6x9 Postcard "401k Rollover" to market Individuals to transfer their retirement savings to our firm

Formats: .jpg, .png, .psd, .ai
Dimensions: See uploaded documents

We need a postcard to encourage people 45-65 years olds to transfer their retirement plan assets to our financial advising firm. We have uploaded an example we've been working please feel free to use your artistic license to make it look good images etc. You do not need to copy it word for word, we welcome creativity.

Suggested Wording:

We make it easy to rollover your old 401k

Spread the word! If you or someone you know has a 401k with a former employer or has reached age 59 1/2, consider a 401k rollover

The Marlowe Financial team can help rollover your old 401k

Advantages of a rollover: control over your accounts, more investment options, professional investment management, consolidate and simplify your accounts, guaranteed lifetime income options, help from a team of dedicated advisors

Make the most of your old 401k with a new Rollover IRA, speak with a trusted advisor today, (661)555-0142

If the QWM logo is used it MUST be used with the name "Gerald Pruitt" near it to clearly associate the two. if the words are used they Must be after his name and in all caps like this "Gerald Pruitt, ACCREDITED WEALTH STEWARD TM" [super script TM]. These are rules of the QWM trade mark.

Target Market(s)

Age 45 to 65 with sizable assets in 401k retirement plans

Industry/Entity Type

Investment Advisory

Font styles to use
Serif
Sans Serif
Decorative
Script

Colors

Designer to choose colors to be used in the design.

Requirements
Must have
• The post card MUST contain the following text at least 8pt font:
• Securities offered through Ember Ridge Securities, L.P. Member - NEVOC/TALQ | 4875 North Elm Rd, Ste 120, Lancaster, CA 93536 | 800.555.0173 | CA Ins. Lic. #0K48391, #0713948, #0K52806, #0619427
• Must have website and phone number:
• www.geraldpruittadvisory.example
• (661) 555-0142
Nice to have
• We would like the design to convey: Trust, Safety, Growth, Wealth, Planning, Strength, Stable, Peace of Mind, Time, Classic, Legacy

```html
<!DOCTYPE html>
<html lang="en">
<head>
<meta charset="utf-8">
<title>Rollover Postcard – Gerald Pruitt</title>
<link href="https://fonts.googleapis.com/css2?family=Oswald:wght@500;600&family=Open+Sans:ital,wght@0,400;0,600;0,700;1,400;1,700&family=Montserrat:wght@800&display=swap" rel="stylesheet">
<style>
:root{
  --indigo:#3f4788;
  --indigo-deep:#343c7a;
  --gold:#c9a063;
  --ink:#1e1e1e;
  --grey:#4a4a4a;
  --paper:#ffffff;
  --backdrop:#e9e9ec;
  --photo-warm:#d9c7a8;
  --photo-light:#efe8dc;
}
*{box-sizing:border-box;margin:0;padding:0}
html,body{width:842px;height:1200px;overflow:hidden;background:var(--backdrop)}
body{position:relative;font-family:"Open Sans",sans-serif;color:var(--ink)}
.card{position:absolute;left:78px;width:680px;height:453px;background:var(--paper);box-shadow:0 6px 16px rgba(0,0,0,.25);overflow:hidden}
.card--front{top:77px}
.card--back{top:665px}

/* front */
.advisor-name{position:absolute;left:32px;top:22px;font-family:"Montserrat",sans-serif;font-weight:800;font-size:25px;letter-spacing:.5px}
.designation{position:absolute;left:32px;top:55px;display:flex;align-items:center;gap:8px}
.designation__mark{font-family:"Montserrat",sans-serif;font-weight:800;font-size:18px;color:var(--ink)}
.designation__words{font-size:7.5px;font-weight:700;letter-spacing:1.6px;line-height:10px;color:var(--ink)}
.hero-band{position:absolute;left:0;top:97px;width:100%;height:284px;background:linear-gradient(90deg,var(--indigo) 60%,var(--indigo-deep))}
.headline{position:absolute;left:37px;top:138px;font-family:"Oswald",sans-serif;font-weight:600;font-size:58px;line-height:70px;color:#fff;letter-spacing:-2px;white-space:nowrap}
.headline .accent{color:var(--gold)}
.hero-photo{position:absolute;left:400px;top:24px;width:280px;height:357px;border-radius:46% 0 0 0;background:linear-gradient(180deg,var(--photo-light),var(--photo-warm))}
.front-contact{position:absolute;right:20px;top:397px;text-align:right}
.front-contact__phone{display:flex;align-items:center;gap:6px;justify-content:flex-end;font-weight:600;font-size:22px}
.front-contact__web{font-style:italic;font-size:11px;color:var(--indigo)}

/* back */
.share-band{position:absolute;left:0;top:0;width:100%;height:111px;background:var(--indigo);color:#fff;text-align:center}
.share-band__title{padding-top:18px;font-weight:700;font-size:30px;letter-spacing:8px}
.share-band__text{margin-top:6px;font-size:16px;line-height:21px}
.share-band__text u{font-weight:700}
.team-strip{position:absolute;left:0;top:111px;width:100%;height:19px;background:var(--gold);color:#fff;font-size:10px;font-weight:600;letter-spacing:1.3px;text-align:center;line-height:19px}
.advantages__title{position:absolute;left:19px;top:155px;font-family:"Montserrat",sans-serif;font-weight:800;font-size:20px;color:var(--indigo);white-space:nowrap}
.advantages__list{position:absolute;left:30px;top:191px;list-style:none;font-size:12px;line-height:18px;color:var(--grey);white-space:nowrap}
.advantages__list li{display:flex;align-items:center;gap:5px}
.cta{position:absolute;left:21px;top:311px;color:var(--grey);white-space:nowrap}
.cta__lead{font-style:italic;font-size:10px;line-height:13.5px}
.cta__call{font-style:italic;font-weight:700;font-size:13.5px;margin-top:2px}
.cta__visit{font-style:italic;font-size:10px}
.cta__web{font-style:italic;font-weight:700;font-size:10.5px;color:var(--ink)}
.couple-photo{position:absolute;left:292px;top:190px;width:116px;height:203px;border-radius:40% 40% 0 0;background:linear-gradient(180deg,var(--photo-light),var(--photo-warm))}
.rule{position:absolute;left:0;top:393px;width:403px;height:2px;background:var(--gold)}
.disclosure{position:absolute;left:11px;top:406px;font-size:8px;line-height:10.6px;color:var(--grey)}
</style>
</head>
<body>

<section class="card card--front">
  <div class="advisor-name">GERALD PRUITT</div>
  <div class="designation">
    <span class="designation__mark">QWM</span>
    <span class="designation__words">ACCREDITED<br>WEALTH<br>STEWARD™</span>
  </div>
  <div class="hero-band"></div>
  <div class="hero-photo" role="img" aria-label="Smiling retired couple, woman hugging man from behind"></div>
  <h1 class="headline">We make it<br>easy to <span class="accent">rollover</span><br>your old <span class="accent">401k</span></h1>
  <div class="front-contact">
    <div class="front-contact__phone">
      <svg width="20" height="20" viewBox="0 0 24 24" aria-hidden="true"><circle cx="12" cy="12" r="10.5" fill="none" stroke="#1e1e1e" stroke-width="2"/><path d="M8.3 6.8l1.6-.3 1.2 2.6-1 1a7 7 0 003.6 3.6l1-1 2.6 1.2-.3 1.6c-.2.6-.8 1-1.4 1A9 9 0 017.3 8.2c0-.6.4-1.2 1-1.4z" fill="#1e1e1e"/></svg>
      (661) 555-0142
    </div>
    <div class="front-contact__web">www.geraldpruittadvisory.example</div>
  </div>
</section>

<section class="card card--back">
  <div class="share-band">
    <div class="share-band__title">SPREAD THE WORD!</div>
    <p class="share-band__text">IF YOU OR SOMEONE YOU KNOW HAS A 401K WITH A FORMER EMPLOYER<br><u>OR</u> HAS REACHED AGE 59 ½, CONSIDER A 401K ROLLOVER</p>
  </div>
  <div class="team-strip">THE MARLOWE FINANCIAL TEAM CAN HELP ROLLOVER YOUR OLD 401K</div>

  <h2 class="advantages__title">ADVANTAGE OF ROLLOVER</h2>
  <ul class="advantages__list">
    <li><svg width="10" height="10" viewBox="0 0 10 10" aria-hidden="true"><rect x="1" y="2" width="7" height="7" rx="1.5" fill="none" stroke="#3f4788"/><path d="M2.5 5.2l1.8 1.8L9 2" fill="none" stroke="#3f4788" stroke-width="1.3"/></svg>Control over your accounts</li>
    <li><svg width="10" height="10" viewBox="0 0 10 10" aria-hidden="true"><rect x="1" y="2" width="7" height="7" rx="1.5" fill="none" stroke="#3f4788"/><path d="M2.5 5.2l1.8 1.8L9 2" fill="none" stroke="#3f4788" stroke-width="1.3"/></svg>More investment options</li>
    <li><svg width="10" height="10" viewBox="0 0 10 10" aria-hidden="true"><rect x="1" y="2" width="7" height="7" rx="1.5" fill="none" stroke="#3f4788"/><path d="M2.5 5.2l1.8 1.8L9 2" fill="none" stroke="#3f4788" stroke-width="1.3"/></svg>Professional investment management</li>
    <li><svg width="10" height="10" viewBox="0 0 10 10" aria-hidden="true"><rect x="1" y="2" width="7" height="7" rx="1.5" fill="none" stroke="#3f4788"/><path d="M2.5 5.2l1.8 1.8L9 2" fill="none" stroke="#3f4788" stroke-width="1.3"/></svg>Consolidate and simplify</li>
    <li><svg width="10" height="10" viewBox="0 0 10 10" aria-hidden="true"><rect x="1" y="2" width="7" height="7" rx="1.5" fill="none" stroke="#3f4788"/><path d="M2.5 5.2l1.8 1.8L9 2" fill="none" stroke="#3f4788" stroke-width="1.3"/></svg>Guaranteed lifetime income options</li>
    <li><svg width="10" height="10" viewBox="0 0 10 10" aria-hidden="true"><rect x="1" y="2" width="7" height="7" rx="1.5" fill="none" stroke="#3f4788"/><path d="M2.5 5.2l1.8 1.8L9 2" fill="none" stroke="#3f4788" stroke-width="1.3"/></svg>Help from a team of dedicated advisors</li>
  </ul>

  <div class="couple-photo" role="img" aria-label="Retired couple standing together, smiling"></div>

  <div class="cta">
    <p class="cta__lead">Make the most of your old 401k with a new Rollover IRA,<br>speak with a trusted advisor,</p>
    <p class="cta__call">call (661) 555-0142</p>
    <p class="cta__visit">or visit our website</p>
    <p class="cta__web">www.geraldpruittadvisory.example</p>
  </div>
  <div class="rule"></div>

  <p class="disclosure">Securities offered through Ember Ridge Securities,<br>L.P. Member - NEVOC/TALQ<br>4875 North Elm Rd, Ste 120, Lancaster, CA 93536 | 800.555.0173<br>CA Ins. Lic. #0K48391, #0713948, #0K52806, #0619427</p>
</section>

</body>
</html>
```